Nutrition-Cooking Website

Hello!
I am in a need of a lovely looking website for my new nutrition practice. I am looking for something sleek, sophisticated, professional yet also welcoming.

Here is a current layout which can be tweaked or overhauled. I feel like the website is not quite what I want so thats why I need your help!!
http://tolvanfolio.example/RENATA-OSSLER-concept-15/

Two websites I like are: (layout similar to www.marquetta.example) or http://www.pernillavostraken.example

Here are the tabs for the website:
About Registered Dietitian Healthy Recipes Philanthropy Shop Features Contact Blog

Features for the Home page include:
Slideshow with 3 rotating updates (like www.marquetta.example)
Video Box (like www.marquetta.example)
Recent Recipes (like http://harrowfield7731.example)
Recent Posts (like http://harrowfield7731.example)
Food Knowledge Box- quick tidbits on laws on food (like www.marquetta.example- she has food wisdom)
Tried and True Benefits of Mediterranean Cuisine (like www.marquetta.example)
Picture of me with brief quote/bio (like www.bettinoruval.example)
Social media buttons

Color Scheme:
• I like the white with gold embroidery or the pretty bluish/purplish in the first pic would be awesome with the slight pink undertones (http://glossedtwirl.example/2012/10/quorvel-marigelle-collection-by-tansley/)
• Also like this goldish background- exotic/sophisticated- http://www.thewhirlingcook.example/Home.html
• Also like the rustic goldish look in the background like this-
ohttp://img.prentlo.example/vexomarks_rsvp_vintage_rustic_gold_swirls_invitation-p161658028764768924bebn6_400.jpg
o http://img.prentlo.example/vexomarks_ornamental_rustic_gold_swirls_invitation-p161776340110432961bvddb_400.jpg
• maybe can have the vines as grapes/olives
OPEN TO ALL DIFFERENT COLORS SCHEMES- whatever looks, clean, sophisticated and professional

Logo:
• Attached is the logo

Budget is flexible. If you think you can improve the website- please do so :)

Target Market(s)

health conscious individuals of all ages

Industry/Entity Type

Embroidery

Requirements
Must have
• clean and sharp look
professional looking
Should not have
• too much busyness

```html
<!DOCTYPE html>
<html lang="en">
<head>
<meta charset="utf-8">
<title>Renata Ossler RD</title>
<link rel="stylesheet" href="https://fonts.googleapis.com/css2?family=Cinzel:wght@500&family=Federo&family=Almendra&family=Montserrat:wght@400;600;700&display=swap">
<style>
:root{
  --page-bg:#f5efe0;
  --cream:#fbe9c8;
  --panel:#fbeedd;
  --orange:#fbb040;
  --gold:#c4962c;
  --red:#e05a4e;
  --dark-red:#a51c1c;
  --green:#2f8f1c;
  --text:#5b5048;
  --heading:#3a2f28;
  --white:#fff;
}
*{box-sizing:border-box;margin:0;padding:0}
html,body{width:876px;height:1200px;overflow:hidden}
body{background:var(--page-bg);font-family:"Montserrat",sans-serif;color:var(--text);position:relative}
.page{position:absolute;left:103px;top:0;width:670px;height:1083px;background:var(--white);box-shadow:0 0 8px rgba(0,0,0,.18)}
.abs{position:absolute}
.hero{left:0;top:0;width:670px;height:321px;background:radial-gradient(circle at 30% 55%,#c24a2c 0,#8e3a22 35%,#b58456 65%,#e2b5a0 100%)}
.logo-band{left:0;top:0}
.logo{left:87px;top:16px;font-family:"Cinzel",serif;font-size:24px;letter-spacing:1px;color:var(--heading)}
.quote{left:428px;top:186px;width:236px;height:129px;background:rgba(60,55,50,.82);text-align:center;color:var(--white)}
.quote h2{font-family:"Federo",sans-serif;font-weight:400;font-size:23px;color:var(--orange);margin-top:8px}
.quote p{font-size:13.5px;line-height:18px;margin:14px 14px 0}
.slider-arrows{left:390px;top:295px}
.nav{left:0;top:321px;width:670px;height:34px;background:linear-gradient(#fcc463,#f9a82d);display:flex}
.nav a{font-family:"Federo",sans-serif;font-size:14px;color:var(--heading);text-decoration:none;line-height:34px;text-align:center;border-right:1px solid #e89524;white-space:nowrap}
.nav a:last-child{border-right:none}
.welcome{left:13px;top:364px;width:426px}
.welcome h3{font-family:"Federo",sans-serif;font-weight:400;font-size:17px;line-height:20px;color:var(--heading)}
.welcome h1{font-family:"Federo",sans-serif;font-weight:400;font-size:22px;line-height:26px;color:var(--red);margin-top:2px}
.welcome p{font-size:9.3px;line-height:15.6px;margin-top:8px}
.read-more{left:387px;top:533px;width:48px;height:16px;border-radius:8px;background:var(--cream);border:1px solid #d9b070;font-size:7.5px;font-weight:600;text-align:center;line-height:14px;color:var(--heading);white-space:nowrap}
.label{font-family:"Federo",sans-serif;font-size:15px;color:var(--red)}
.photo{border:3px solid var(--orange)}
.card-tag{left:0;top:6px;padding:3px 7px;font-family:"Federo",sans-serif;font-size:14px;color:var(--white);white-space:nowrap}
.newsletter{left:452px;top:565px;width:204px;height:161px;background:linear-gradient(#5a2a1c,#3a1a12);border:2px solid #b0281c}
.register{left:0;top:0;width:126px;height:68px;background:var(--green);border-radius:0 0 40px 0;color:var(--white);font-weight:600;font-size:15px;line-height:17px;padding:6px 6px;white-space:nowrap}
.click-here{left:132px;top:10px;background:var(--orange);color:var(--heading);font-size:9.5px;font-weight:700;padding:4px 6px;border-radius:2px;white-space:nowrap}
.join{left:6px;top:74px;color:var(--white);font-weight:600;font-size:14px;white-space:nowrap}
.email{left:6px;top:96px;width:188px;height:25px;background:var(--white);font-size:9px;color:#999;padding:7px 8px}
.subscribe{left:106px;top:131px;width:92px;height:24px;background:var(--orange);color:var(--white);font-weight:700;font-size:15px;text-align:center;line-height:24px}
.panel{top:739px;width:316px;height:325px;background:var(--panel)}
.panel h4{font-family:"Almendra",serif;font-weight:400;font-size:21px;color:var(--heading);text-align:center;margin-top:10px}
.rule{display:block;margin:3px auto 0}
.post{left:12px;width:296px;height:100px}
.post .thumb{left:0;top:0;width:118px;height:100px;background:linear-gradient(135deg,#f6e1a0,#f0b14a 55%,#c82d2d);border:2px solid #fff}
.date{left:0;top:2px;width:34px;background:var(--dark-red);color:var(--white);text-align:center;font-weight:700;font-size:13px;line-height:13px;padding-top:2px}
.date small{display:block;background:#fff;color:var(--dark-red);font-size:8px;line-height:10px}
.post h5{left:131px;top:0;width:160px;font-size:11.5px;line-height:14px;font-weight:700;color:var(--heading)}
.post p{left:131px;top:48px;width:160px;font-size:7.6px;line-height:10.5px}
.share{left:131px;top:94px;font-size:6px;font-weight:600;color:var(--heading);white-space:nowrap}
.more{left:250px;top:94px;font-size:7.6px;color:var(--text);white-space:nowrap}
.recipe-img{left:14px;top:70px;width:287px;height:99px;background:linear-gradient(90deg,#b86a18,#e8a33c 40%,#6e9a3a 70%,#9b3a5a);border:3px solid var(--orange)}
.recipe h5{left:14px;top:186px;font-size:12px;font-weight:700;color:var(--heading);width:290px;line-height:14px}
.recipe p{left:14px;top:219px;width:290px;font-size:9px;line-height:13.5px}
.view-all{left:117px;top:286px;width:88px;height:25px;background:linear-gradient(#d5a440,#a37720);border:1px solid #8c6418;border-radius:3px;color:var(--white);font-weight:600;font-size:15px;text-align:center;line-height:23px}
.footer{position:absolute;left:0;top:1083px;width:876px;height:117px;background:var(--gold)}
.foot-nav{position:absolute;top:6px;left:0;width:876px;text-align:center;font-size:9.5px;font-weight:600;color:var(--white)}
.foot-nav span{margin:0 7px}
.copy{position:absolute;top:24px;width:876px;text-align:center;font-size:8.5px;color:#fbe9c0}
.follow{position:absolute;top:52px;width:876px;text-align:center;font-size:14px;color:#3e3020}
.social{position:absolute;top:76px;width:876px;text-align:center;font-size:12px;font-weight:700;color:#3e3020}
.social span{margin:0 6px}
</style>
</head>
<body>
<div class="page">
  <header>
    <div class="abs hero" role="img" aria-label="Photo of appetizers: salami, tomato and olive bites on bread in a basket"></div>
    <svg class="abs logo-band" width="670" height="80" viewBox="0 0 670 80" aria-hidden="true">
      <path d="M0 0H670V8C560 30 470 55 330 72C200 80 90 70 0 48Z" fill="#fbe4bb"/>
      <path d="M0 48C90 70 200 80 330 72C470 55 560 30 670 8" fill="none" stroke="#e9c37a" stroke-width="2"/>
    </svg>
    <div class="abs logo">Renata Ossler RD</div>
    <div class="abs quote">
      <h2>Vivian Marlowe</h2>
      <p>one cannot think well, love well, sleep well, if one has not dined well.</p>
    </div>
    <svg class="abs slider-arrows" width="34" height="20" viewBox="0 0 34 20" aria-hidden="true">
      <rect width="34" height="20" fill="rgba(60,55,50,.6)"/>
      <path d="M12 5L7 10L12 15M22 5L27 10L22 15" fill="none" stroke="#fff" stroke-width="1.5"/>
    </svg>
    <nav class="abs nav">
      <a style="width:58px">About</a>
      <a style="width:148px">Registered Dietitian</a>
      <a style="width:122px">Healthy Recipes</a>
      <a style="width:103px">Philanthropy</a>
      <a style="width:51px">Shop</a>
      <a style="width:71px">Feature</a>
      <a style="width:70px">Contact</a>
      <a style="width:47px">Blog</a>
    </nav>
  </header>

  <section class="abs welcome">
    <h3>Welcome to</h3>
    <h1>Renata Ossler RD</h1>
    <p>This is Pixelcraft's version of Lorem Ipsum. Proin gravida nibh vel velit auctor aliquet. Aenean sollicitudin, lorem quis bibendum auctor, nisi elit consequat ipsum, nec sagittis sem nibh id elit. Duis sed odio sit amet nibh vulputate cursus a sit amet mauris. Morbi accumsan ipsum velit. Nam nec tellus a odio tincidunt auctor a ornare odio. Sed non mauris vitae erat consequat auctor eu in elit. Class aptent taciti sociosqu ad litora torquent per conubia nostra, per inceptos himenaeos. Mauris in erat justo. Nullam ac urna eu felis dapibus condimentum sit amet a augue.</p>
  </section>
  <div class="abs read-more">Read more</div>

  <div class="abs label" style="left:458px;top:366px">Video</div>
  <div class="abs photo" style="left:452px;top:394px;width:204px;height:155px;background:linear-gradient(#9fc3e0,#c9b89a 50%,#6f8f4a)" role="img" aria-label="Video still: a family sharing a meal at an outdoor table"></div>

  <div class="abs photo" style="left:13px;top:565px;width:205px;height:161px;background:radial-gradient(circle at 50% 60%,#9c3a2a,#7fae3a 45%,#e9f0d8 80%)" role="img" aria-label="Photo of a fresh salad on a plate">
    <div class="abs card-tag" style="background:var(--dark-red)">Food Knowledge</div>
  </div>
  <div class="abs photo" style="left:231px;top:565px;width:206px;height:161px;background:linear-gradient(#e6e2d8,#b9c9a8 55%,#c85a3a)" role="img" aria-label="Photo of a woman at an open fridge full of fresh produce">
    <div class="abs card-tag" style="background:var(--green)">Food Philosophy</div>
  </div>

  <div class="abs newsletter">
    <div class="abs register">Register<br>for cooking<br>classes</div>
    <div class="abs click-here">Click Here</div>
    <div class="abs join">Join Renata's Newsletter</div>
    <div class="abs email">Email-Id</div>
    <div class="abs subscribe">Subscribe</div>
  </div>

  <section class="abs panel" style="left:13px">
    <h4>Recent Post</h4>
    <svg class="rule" width="190" height="8" viewBox="0 0 190 8" aria-hidden="true"><line x1="0" y1="4" x2="190" y2="4" stroke="#c4962c"/><rect x="91" y="0" width="8" height="8" transform="rotate(45 95 4)" fill="#c4962c"/></svg>
    <article class="abs post" style="top:69px">
      <div class="abs thumb" role="img" aria-label="Photo of a fruit smoothie with strawberries and mint"></div>
      <div class="abs date">05<small>MAR</small></div>
      <h5 class="abs">Pomegranate chocolate cupcakes with buttercream frosting</h5>
      <p class="abs">This is Pixelcraft's version of Lorem Ipsum. Proin gravida nibh vel velit auctor aliquet.</p>
      <div class="abs share">Netlane · Friendsheet · Chirpway</div>
      <div class="abs more">View more ›</div>
    </article>
    <article class="abs post" style="top:197px">
      <div class="abs thumb" role="img" aria-label="Photo of a fruit smoothie with strawberries and mint"></div>
      <div class="abs date">05<small>MAR</small></div>
      <h5 class="abs">Pomegranate chocolate cupcakes with buttercream frosting</h5>
      <p class="abs">This is Pixelcraft's version of Lorem Ipsum. Proin gravida nibh vel velit auctor aliquet.</p>
      <div class="abs share">Netlane · Friendsheet · Chirpway</div>
      <div class="abs more">View more ›</div>
    </article>
  </section>

  <section class="abs panel recipe" style="left:341px">
    <h4>Recent Recipes</h4>
    <svg class="rule" width="190" height="8" viewBox="0 0 190 8" aria-hidden="true"><line x1="0" y1="4" x2="190" y2="4" stroke="#c4962c"/><rect x="91" y="0" width="8" height="8" transform="rotate(45 95 4)" fill="#c4962c"/></svg>
    <div class="abs recipe-img" role="img" aria-label="Photo of breaded fried fish with a side salad"></div>
    <h5 class="abs">Pomegranate chocolate cupcakes with buttercream frosting</h5>
    <p class="abs">This is Pixelcraft's version of Lorem Ipsum. Proin gravida nibh vel velit auctor aliquet. Aenean sollicitudin, lorem quis bibendum auctor, nisi elit consequat ipsum, nec sagittis sem nibh id elit.</p>
    <div class="abs view-all">View All</div>
  </section>
</div>

<footer class="footer">
  <div class="foot-nav"><span>About</span><span>Registered Dietitian</span><span>Healthy Recipes</span><span>Philanthropy</span><span>Shop</span><span>Feature</span><span>Contact</span><span>Blog</span></div>
  <div class="copy">Copyright © 2013 Renata Ossler RD &nbsp;&nbsp; Terms and Conditions &nbsp; | &nbsp; Sitemap</div>
  <div class="follow">Follow us on</div>
  <div class="social"><span>Chirpway</span><span>Netlane</span><span>Friendsheet</span></div>
</footer>
</body>
</html>
```